Design some Business Cards for Wendlocks

Hi everyone,

We are in need of a new business card design. Artwork is to be in 3 colours - white, black and orange. I have attached a photo of the colours I would like. The logo is attached as an EPS & PDF. Size of the card is to be slimline 90x45mm landscape.

There is an opportunity for ongoing work for the winning freelancer.

We will require on the card:
Person's Name
Company Position
Mobile/Cell Phone Number
Office Phone Number
Email Address
Website
Street Address

```html
<!DOCTYPE html>
<html lang="en">
<head>
<meta charset="utf-8">
<title>Wendlocks Business Cards</title>
<link rel="stylesheet" href="https://fonts.googleapis.com/css2?family=Open+Sans:wght@300;400;600&display=swap">
<style>
  :root {
    --bg: #ececec;
    --black: #0c0c0c;
    --black-soft: #1e1e1e;
    --orange: #f07a2c;
    --orange-light: #f79a55;
    --white: #ffffff;
    --ink: #2a1a10;
  }
  * { margin: 0; padding: 0; box-sizing: border-box; }
  html, body {
    width: 1200px; height: 912px; overflow: hidden;
    background: var(--bg);
    font-family: "Open Sans", Arial, sans-serif;
  }
  .sheet {
    position: relative; width: 1200px; height: 912px;
    display: flex; flex-direction: column; align-items: center; justify-content: center; gap: 40px;
  }
  .card {
    position: relative; width: 820px; height: 410px; overflow: hidden;
    box-shadow: 0 6px 18px rgba(0,0,0,0.18);
  }
  /* front */
  .card-front { display: flex; }
  .brand-panel {
    width: 470px; height: 100%;
    background: linear-gradient(135deg, var(--black-soft), var(--black));
    display: flex; align-items: center; justify-content: center;
  }
  .brand-name {
    color: var(--orange); font-weight: 600; font-size: 64px; letter-spacing: 1px;
  }
  .icon-strip {
    position: relative; width: 34px; height: 100%; background: var(--white);
    border-left: 6px solid var(--white);
  }
  .icon-strip::before {
    content: ""; position: absolute; left: 4px; top: 0; bottom: 0; width: 2px; background: var(--black);
  }
  .icon-list {
    position: absolute; left: 8px; top: 292px; display: flex; flex-direction: column; gap: 14px;
  }
  .icon-list svg { display: block; width: 16px; height: 16px; }
  .info-panel {
    position: relative; flex: 1; height: 100%;
    background: linear-gradient(160deg, var(--orange-light), var(--orange));
    padding: 46px 0 0 36px; color: var(--white);
  }
  .pointer {
    position: absolute; left: 0; top: 56px; width: 0; height: 0;
    border-top: 14px solid transparent; border-bottom: 14px solid transparent;
    border-left: 16px solid var(--black);
  }
  .person-name { font-weight: 300; font-size: 28px; letter-spacing: 1px; line-height: 1.1; }
  .person-role { font-weight: 400; font-size: 16px; color: var(--ink); margin-top: 2px; }
  .contact-list {
    position: absolute; left: 36px; top: 288px; list-style: none;
    font-size: 15px; line-height: 30px; font-weight: 400;
  }
  /* back */
  .card-back {
    background: linear-gradient(135deg, var(--black-soft), var(--black));
    display: flex; align-items: center; justify-content: center;
  }
  .back-brand { color: var(--orange); font-weight: 600; font-size: 96px; letter-spacing: 1px; }
  .back-web {
    position: absolute; left: 0; right: 0; bottom: 62px; text-align: center;
    color: var(--orange); font-size: 15px; padding-left: 180px;
  }
</style>
</head>
<body>
<main class="sheet">
  <section class="card card-front">
    <div class="brand-panel"><span class="brand-name">Wendlocks</span></div>
    <div class="icon-strip">
      <div class="icon-list">
        <svg viewBox="0 0 16 16" aria-label="phone"><path d="M4 1.5l2.3 2.8-1.3 1.6c.9 2 2.6 3.7 4.6 4.6l1.6-1.3 2.8 2.3-1.5 2.5C7 13.6 2.4 9 1.5 3z" fill="var(--black)"/></svg>
        <svg viewBox="0 0 16 16" aria-label="email"><circle cx="8" cy="8" r="6.2" fill="none" stroke="var(--black)" stroke-width="1.6"/><circle cx="8" cy="8" r="2.4" fill="none" stroke="var(--black)" stroke-width="1.6"/></svg>
        <svg viewBox="0 0 16 16" aria-label="web"><circle cx="8" cy="8" r="6.2" fill="none" stroke="var(--black)" stroke-width="1.6"/><path d="M1.8 8h12.4M8 1.8c-3 3.5-3 8.9 0 12.4M8 1.8c3 3.5 3 8.9 0 12.4" fill="none" stroke="var(--black)" stroke-width="1.2"/></svg>
        <svg viewBox="0 0 16 16" aria-label="address"><path d="M8 1.5L1 8h2v6.5h4V10h2v4.5h4V8h2z" fill="var(--black)"/></svg>
      </div>
    </div>
    <div class="info-panel">
      <span class="pointer"></span>
      <p class="person-name">MARA QUINN</p>
      <p class="person-role">Manager</p>
      <ul class="contact-list">
        <li>555 018 2044</li>
        <li>mara@wendlocks.com</li>
        <li>www.wendlocks.com</li>
        <li>Address line1  Adress line2</li>
      </ul>
    </div>
  </section>

  <section class="card card-back">
    <span class="back-brand">Wendlocks</span>
    <p class="back-web">www.wendlocks.com</p>
  </section>
</main>
</body>
</html>
```